Business Card Design

I would like a new business card design for an accounting firm that specializes in resolving clients tax problems. I want the card to give the impression that we are not your typical stodgy accounting firm, but at the same time we will get the job done.
Industry/Entity Type
Business
Contact Information for Business Card
Dorian T Welsby
Certified Public Accountant
38-27 52nd Street
Sunnyside, NY 11287
Tel: (718) 555-0142
Fax: (888) 555-0199
e-mail: dtwthecpa@ledgerpost.com
website: harborfilingreliefexperts.com

```html
<!DOCTYPE html>
<html lang="en">
<head>
<meta charset="utf-8">
<title>Dorian T Welsby – Business Card</title>
<link rel="stylesheet" href="https://fonts.googleapis.com/css2?family=Fira+Sans:wght@300;400;600;700&display=swap">
<style>
  :root {
    --backdrop: #b9babc;
    --card: #ffffff;
    --ink: #1c1c1e;
    --text: #2a2a2c;
    --accent: #1a8fd1;
  }
  * { margin: 0; padding: 0; box-sizing: border-box; }
  html, body {
    width: 1200px;
    height: 900px;
    overflow: hidden;
    background: var(--backdrop);
  }
  body {
    display: flex;
    align-items: center;
    justify-content: center;
    font-family: "Fira Sans", sans-serif;
  }
  .business-card {
    position: relative;
    width: 840px;
    height: 480px;
    background: var(--card);
    box-shadow: 0 10px 30px rgba(0, 0, 0, 0.18);
  }
  .card-identity {
    position: absolute;
    left: 210px;
    top: 96px;
  }
  .card-name {
    font-weight: 700;
    font-size: 40px;
    letter-spacing: 0.5px;
    color: var(--ink);
    line-height: 1.1;
  }
  .card-title {
    margin-top: 10px;
    font-weight: 400;
    font-size: 27px;
    color: var(--accent);
    letter-spacing: 0.3px;
  }
  .card-contact {
    position: absolute;
    left: 210px;
    top: 236px;
    list-style: none;
    font-size: 21px;
    font-weight: 300;
    color: var(--text);
    line-height: 33px;
  }
  .card-contact .address { margin-bottom: 4px; }
  .contact-label { color: var(--accent); }
  .card-website {
    position: absolute;
    left: 300px;
    top: 412px;
    font-size: 21px;
    font-weight: 300;
    color: var(--text);
    letter-spacing: 0.4px;
  }
</style>
</head>
<body>
  <article class="business-card">
    <header class="card-identity">
      <h1 class="card-name">Dorian T Welsby</h1>
      <p class="card-title">Certified Public Accountant</p>
    </header>
    <ul class="card-contact">
      <li class="address">38-27 52nd Street Sunnyside, NY 11287</li>
      <li><span class="contact-label">Tel:</span> (718) 555-0142</li>
      <li><span class="contact-label">Fax:</span> (888) 555-0199</li>
      <li><span class="contact-label">e-mail:</span> dtwthecpa@ledgerpost.com</li>
    </ul>
    <p class="card-website">www.harborfilingreliefexperts.com</p>
  </article>
</body>
</html>
```